依頼詳細
<現状の課題>
①一目で、メガネ・コンタクトの取扱いのお店とわからない。
※地域密着型(関東近郊)で隣に眼科が併設されている店舗になります。
②ターゲットにあったサイトデザインになってない。
(詳細は添付”コンセプトワーク”を参照ください)

<現在のサイト>
明確なHPの情報共有はできませんが、トップページの情報を一部伏せて共有します。
添付 ”トップページ” を参照ください。

<イメージサイト>
http://www.kumoringo.jp/
写真多めのポップデザインとして
http://www2.tanpopoko.co.jp/
コンテンツの配置やメインターゲットへの訴求の仕方
http://www.mufuta.jp/
商品、店舗(施設)の見せ方

<重視する点/検討基準>
① デザイン性(ペルソナにあったデザイン)
② 納期厳守

<具体的な制作数>
TOPページ:1ページ

<選考の進め方>
ご提案頂いたデザイン内容・コンセプトなどをもとに、プロジェクトメンバーで選考、決定致します。
※今回は、トップページのデザインのみの見積もりとなります。
今後、コーディングを依頼する可能性もございます。(別途見積もり)

以上です。
Pivoraの皆さまからの、素晴らしい提案をお待ちしております。
宜しくお願い致します。
ページ数
1ページ
希望イメージ
シンプル 複雑
単色 カラフル
暗い 明るい
日常 高級
遊び心 厳粛
未来的 伝統的
女性的 男性的
希望する色
緑系、黄・オレンジ系、コンセプトカラー(ホワイト6割、グリーン3割、オレンジ1割の配色 ※あくまで弊社のイメージです)
納品ファイル
• イラストレーター形式 (.ai)
• フォトショップ形式 (.psd)
補足説明
コンセプトカラーもこれから決めていくため、自由に提案頂きたいです。
現在はメインとなるコンセプトカラーを3色ほどで考えています。
依頼公開後の追記内容
※提案数によっては期限延長する場合がございますのでご容赦ください。
※期限6/9⇒6/11へ延長致します。
選定時期は順次報告致します。
ご提案頂いておりました皆様へ

今回、7/2選定期限となっておりましたが、
弊社での選定に時間がかかっております。

誠に申し訳ございませんが、
7/8に期間延長をさせて頂きました。

今しばらくお待ちくださいませ。
今後ともよろしくお願い致します。
■ 選んだ理由

当選:hikaru7721様
次点:tovelin様、pomme_grise様
クライアント様と協議させて頂き、総合的なバランスを評価させて頂きました。
その中で、1番クライアント様からお声が多かった「hikaru7721様」を当選とさせていただきました。ありがとうございました。

■ 提案者全員のお礼・コメント

いずれもそれぞれに良いものがあり、大いに悩んで選択させて頂きました。ご提案頂いた皆様に心より感謝申し上げます。

また、今回選定が遅れてしまったこと大変申し訳ございませんでした。

機会があれば、今後ともよろしくお願い致します。

```html
<!DOCTYPE html>
<html lang="ja">
<head>
<meta charset="utf-8">
<title>ひかり眼鏡 トップページ</title>
<link href="https://fonts.googleapis.com/css2?family=M+PLUS+Rounded+1c:wght@400;700;800&family=Noto+Sans+JP:wght@400;700&display=swap" rel="stylesheet">
<style>
:root{
  --green:#8cc63f;
  --green-dark:#6fa52a;
  --teal:#1fa48f;
  --teal-dark:#1e6b63;
  --pink:#e0416f;
  --orange:#f39a1e;
  --blue:#2b6fae;
  --text:#555;
  --muted:#999;
  --line:#e3e3e3;
  --bg:#f4f4f2;
  --white:#fff;
}
*{box-sizing:border-box;margin:0;padding:0}
html,body{width:769px;height:1200px;overflow:hidden}
body{background:var(--bg);font-family:"Noto Sans JP",sans-serif;color:var(--text);font-size:10px;position:relative}
a{color:inherit;text-decoration:none}

.site-header{position:absolute;left:0;top:0;width:769px;height:72px;background:var(--white)}
.brand{position:absolute;left:10px;top:8px;display:flex;align-items:center;gap:6px}
.brand-mark{width:30px;height:30px;background:var(--green);border-radius:4px}
.brand-name{font-family:"M PLUS Rounded 1c",sans-serif;font-weight:800;font-size:20px;color:var(--green-dark)}
.brand-tag{position:absolute;left:10px;top:48px;font-size:9px;color:var(--muted)}
.header-lead{position:absolute;left:178px;top:16px;width:210px;font-size:8px;line-height:1.5;color:var(--muted)}
.util-links{position:absolute;right:14px;top:4px;display:flex;gap:14px;font-size:8px;color:var(--muted)}
.tel{position:absolute;left:418px;top:20px;display:flex;align-items:center;gap:8px}
.tel-icon{width:38px;height:38px;border-radius:50%;background:var(--orange);display:flex;align-items:center;justify-content:center}
.tel-num{font-family:"M PLUS Rounded 1c",sans-serif;font-weight:800;font-size:26px;color:var(--orange);line-height:1}
.tel-hours{font-size:8px;color:var(--muted);margin-top:3px}
.contact-btn{position:absolute;right:14px;top:20px;width:78px;height:44px;background:var(--green);color:var(--white);font-size:9px;font-weight:700;display:flex;flex-direction:column;align-items:center;justify-content:center;border-radius:3px}

.global-nav{position:absolute;left:0;top:74px;width:769px;height:24px;background:#ececea;border-bottom:2px solid var(--green);display:flex}
.global-nav a{flex:1;display:flex;align-items:center;justify-content:center;gap:5px;font-size:9px;color:var(--text);border-right:1px solid #d6d6d6}
.global-nav a.current{background:var(--green);color:var(--white)}
.nav-dot{width:8px;height:8px;border-radius:50%;background:var(--green)}
.current .nav-dot{background:var(--white)}

.hero{position:absolute;left:0;top:98px;width:769px;height:282px;background:var(--white)}
.hero-photo{position:absolute;left:0;top:0;width:380px;height:282px;background:linear-gradient(180deg,#e8e4de 0%,#d9d1c5 55%,#b7a48c 100%)}
.hero-copy{position:absolute;left:24px;top:40px;font-size:10px;line-height:1.7;color:#666}
.hero-list{position:absolute;left:386px;top:8px;width:376px}
.hero-item{display:flex;gap:8px;height:88px;align-items:flex-start;border-bottom:1px solid var(--line);padding-top:6px}
.hero-thumb{width:120px;height:70px;flex:none}
.hero-item p{font-size:10px;line-height:1.6;color:#666;padding-top:6px}

.news{position:absolute;left:0;top:384px;width:769px;height:26px;background:var(--white);display:flex;align-items:center;border-top:1px solid var(--line);border-bottom:1px solid var(--line)}
.news-label{background:var(--green);color:var(--white);font-size:9px;font-weight:700;height:100%;width:70px;display:flex;align-items:center;justify-content:center}
.news-text{margin-left:16px;font-size:9px}

.section-title{position:absolute;left:12px;top:420px;font-family:"M PLUS Rounded 1c",sans-serif;font-size:22px;letter-spacing:3px;color:#dcdcd8}

.contents{position:absolute;left:12px;top:454px;width:745px;display:grid;grid-template-columns:repeat(3,241px);gap:12px;row-gap:14px}
.card{background:var(--white);height:215px;display:flex;flex-direction:column;align-items:center;padding-top:22px;border:1px solid var(--line)}
.card-icon{width:92px;height:92px;border-radius:50%;display:flex;align-items:center;justify-content:center}
.card-title{font-family:"M PLUS Rounded 1c",sans-serif;font-weight:800;font-size:19px;margin-top:14px}
.card-text{font-size:8px;color:var(--muted);line-height:1.6;margin-top:8px;padding:0 22px;text-align:center}
.c-green{--c:var(--green)}
.c-pink{--c:var(--pink)}
.c-teal{--c:var(--teal)}
.c-orange{--c:var(--orange)}
.c-dark{--c:var(--teal-dark)}
.card-icon{background:var(--c)}
.card-title{color:var(--c)}

.banners{position:absolute;left:12px;top:916px;width:745px;display:flex;gap:12px}
.banner{flex:1;height:104px;background:var(--white);border:1px solid var(--line);display:flex;align-items:center;gap:16px;padding-left:26px}
.banner-icon{width:50px;height:50px;flex:none;display:flex;align-items:center;justify-content:center}
.banner-title{font-family:"M PLUS Rounded 1c",sans-serif;font-weight:800;font-size:17px}
.banner-text{font-size:8px;color:var(--muted);margin-top:6px;line-height:1.5}
.banner.recruit .banner-icon{background:var(--blue);border-radius:50%}
.banner.recruit .banner-title{color:var(--blue)}
.banner.about .banner-icon{background:var(--orange);border-radius:4px}
.banner.about .banner-title{color:var(--orange)}

.site-footer{position:absolute;left:0;top:1036px;width:769px;height:164px;background:var(--green);color:var(--white)}
.to-top{position:absolute;right:14px;top:-26px;width:52px;height:52px;border-radius:50%;background:var(--green);display:flex;align-items:center;justify-content:center;border:3px solid var(--bg)}
.footer-cols{position:absolute;left:40px;top:16px;display:flex;gap:60px;font-size:9px;line-height:1.75}
.footer-cols h4{font-size:9px;font-weight:700}
.footer-company{position:absolute;left:470px;top:16px;font-size:9px;line-height:1.75}
.footer-company strong{font-size:11px}
.copyright{position:absolute;left:0;bottom:8px;width:100%;text-align:center;font-size:8px;opacity:.9}
</style>
</head>
<body>

<header class="site-header">
  <a class="brand" href="#"><span class="brand-mark"></span><span class="brand-name">ひかり眼鏡</span></a>
  <p class="brand-tag">みんなの街のめがね屋さん</p>
  <p class="header-lead">メガネ・コンタクトのことならお任せください。<br>眼科が隣接しているので検査から購入まで安心。<br>地域の皆さまの見えるを毎日支えています。</p>
  <nav class="util-links"><a href="#">サイトマップ</a><a href="#">会社概要</a><a href="#">お問い合わせ</a></nav>
  <div class="tel">
    <span class="tel-icon"><svg width="20" height="20" viewBox="0 0 24 24"><path d="M6.6 10.8a15 15 0 0 0 6.6 6.6l2.2-2.2a1 1 0 0 1 1-.25 11.4 11.4 0 0 0 3.6.57 1 1 0 0 1 1 1V20a1 1 0 0 1-1 1A17 17 0 0 1 3 4a1 1 0 0 1 1-1h3.5a1 1 0 0 1 1 1c0 1.25.2 2.45.57 3.57a1 1 0 0 1-.25 1z" fill="#fff"/></svg></span>
    <div><div class="tel-num">0120-00-0000</div><div class="tel-hours">受付時間 10:00〜19:00 (年中無休)</div></div>
  </div>
  <a class="contact-btn" href="#"><svg width="18" height="14" viewBox="0 0 18 14"><rect x="1" y="1" width="16" height="12" fill="none" stroke="#fff" stroke-width="1.5"/><path d="M1 1l8 7 8-7" fill="none" stroke="#fff" stroke-width="1.5"/></svg>CONTACTS</a>
</header>

<nav class="global-nav">
  <a class="current" href="#"><span class="nav-dot"></span>HOME</a>
  <a href="#"><span class="nav-dot"></span>初めての方へ</a>
  <a href="#"><span class="nav-dot"></span>メガネ</a>
  <a href="#"><span class="nav-dot"></span>コンタクトレンズ</a>
  <a href="#"><span class="nav-dot"></span>ネットショップ</a>
  <a href="#"><span class="nav-dot"></span>店舗情報</a>
  <a href="#"><span class="nav-dot"></span>求人情報</a>
</nav>

<section class="hero">
  <div class="hero-photo" role="img" aria-label="木のテーブルに置かれたメガネの写真"></div>
  <p class="hero-copy">地域密着の眼鏡店として<br>あなたにぴったりの一本をご提案します</p>
  <div class="hero-list">
    <div class="hero-item"><div class="hero-thumb" role="img" aria-label="並んだメガネフレームの写真" style="background:linear-gradient(135deg,#dfe3e6,#9aa3aa)"></div><p>新モデル入荷しました！今年のトレンドを<br>一番乗りで手に入れましょう</p></div>
    <div class="hero-item"><div class="hero-thumb" role="img" aria-label="パソコン作業の写真" style="background:linear-gradient(135deg,#d5e4f0,#7d9bb3)"></div><p>ブルーライトカットのレンズって、本当に<br>効いているの？その疑問にお答えします</p></div>
    <div class="hero-item" style="border-bottom:none"><div class="hero-thumb" role="img" aria-label="コンタクトレンズを持つ手元の写真" style="background:linear-gradient(135deg,#f1e3da,#c9a48f)"></div><p>あなたに一番あったコンタクトレンズは？<br>ライフスタイルに合わせて選びましょう</p></div>
  </div>
</section>

<div class="news"><span class="news-label">新着情報</span><span class="news-text">新モデル入荷しました！今年のトレンドを一番乗りで手に入れましょう</span></div>

<h2 class="section-title">contents.</h2>

<main class="contents">
  <a class="card c-green" href="#">
    <span class="card-icon"><svg width="44" height="44" viewBox="0 0 24 24"><circle cx="12" cy="12" r="10" fill="none" stroke="#fff" stroke-width="2"/><rect x="11" y="10" width="2" height="8" fill="#fff"/><circle cx="12" cy="7" r="1.3" fill="#fff"/></svg></span>
    <span class="card-title">はじめての方はこちら</span>
    <p class="card-text">当店のご利用方法や検査の流れを、わかりやすくご紹介しています。はじめての方も安心です。</p>
  </a>
  <a class="card c-pink" href="#">
    <span class="card-icon"><svg width="56" height="30" viewBox="0 0 56 30"><circle cx="14" cy="15" r="10" fill="none" stroke="#fff" stroke-width="3"/><circle cx="42" cy="15" r="10" fill="none" stroke="#fff" stroke-width="3"/><path d="M24 13q4-4 8 0" fill="none" stroke="#fff" stroke-width="3"/></svg></span>
    <span class="card-title">シーン別おすすめメガネ</span>
    <p class="card-text">仕事用、運転用、おしゃれ用など、使う場面に合わせたメガネ選びのコツをお伝えします。</p>
  </a>
  <a class="card c-teal" href="#">
    <span class="card-icon"><svg width="46" height="40" viewBox="0 0 24 22"><path d="M1 2h4l3 12h12l2-9H7" fill="none" stroke="#fff" stroke-width="2" stroke-linejoin="round"/><circle cx="10" cy="18" r="2" fill="#fff"/><circle cx="18" cy="18" r="2" fill="#fff"/></svg></span>
    <span class="card-title">コンタクトレンズ通販</span>
    <p class="card-text">いつものレンズをネットで簡単注文。ご自宅までお届けする便利なサービスです。</p>
  </a>
  <a class="card c-orange" href="#">
    <span class="card-icon"><svg width="44" height="40" viewBox="0 0 24 22"><path d="M2 11L12 2l10 9" fill="none" stroke="#fff" stroke-width="2.4"/><path d="M5 10v11h14V10" fill="#fff"/><rect x="10" y="14" width="4" height="7" fill="var(--orange)"/></svg></span>
    <span class="card-title">店舗情報</span>
    <p class="card-text">関東近郊の各店舗の所在地、営業時間、駐車場情報などをご案内しています。</p>
  </a>
  <a class="card c-dark" href="#">
    <span class="card-icon"><svg width="40" height="40" viewBox="0 0 24 24"><path d="M9 2h6v7h7v6h-7v7H9v-7H2V9h7z" fill="#fff"/></svg></span>
    <span class="card-title">隣接眼科で診察できます</span>
    <p class="card-text">店舗の隣に眼科があるので、診察から処方、レンズ選びまでスムーズです。</p>
  </a>
  <a class="card c-orange" href="#">
    <span class="card-icon"><svg width="40" height="44" viewBox="0 0 24 26"><path d="M3 2l9 11 9-11M12 13v12M5 15h14M5 20h14" fill="none" stroke="#fff" stroke-width="3"/></svg></span>
    <span class="card-title">お得なクーポン</span>
    <p class="card-text">今月のお得なクーポンを配信中。ご来店の際に画面を見せてご利用ください。</p>
  </a>
</main>

<section class="banners">
  <a class="banner recruit" href="#">
    <span class="banner-icon"><svg width="24" height="24" viewBox="0 0 24 24"><path d="M4 20L20 4M14 4h6v6" fill="none" stroke="#fff" stroke-width="2.4"/></svg></span>
    <div><div class="banner-title">スタッフ募集 / 採用情報</div><p class="banner-text">私たちと一緒に地域の見えるを支えませんか？<br>経験不問、研修制度も充実しています。</p></div>
  </a>
  <a class="banner about" href="#">
    <span class="banner-icon"><svg width="24" height="24" viewBox="0 0 24 24"><rect x="5" y="4" width="14" height="17" fill="none" stroke="#fff" stroke-width="2"/><path d="M9 9h2M13 9h2M9 13h2M13 13h2" stroke="#fff" stroke-width="2"/></svg></span>
    <div><div class="banner-title">ひかり眼鏡はこんなお店です</div><p class="banner-text">創業からの想いやスタッフの紹介、<br>お店のこだわりをご紹介します。</p></div>
  </a>
</section>

<footer class="site-footer">
  <a class="to-top" href="#"><svg width="22" height="14" viewBox="0 0 22 14"><path d="M2 12l9-9 9 9" fill="none" stroke="#fff" stroke-width="3"/></svg></a>
  <div class="footer-cols">
    <div><h4>商品情報</h4>初めての方へ<br>メガネ<br>コンタクトレンズ<br>コンタクト通販<br>クーポン</div>
    <div><h4>企業情報</h4>店舗一覧<br>会社概要<br>採用情報<br>お問い合わせ<br>プライバシーポリシー<br>サイトマップ</div>
  </div>
  <div class="footer-company"><strong>株式会社ひかり眼鏡</strong><br>〒000-0000 東京都千代田区光の町1-2-3<br>TEL 0120-00-0000<br>info@hikari-megane.example</div>
  <p class="copyright">Copyright © ひかり眼鏡 All rights reserved.</p>
</footer>

</body>
</html>
```